HarmoNest Ensemble Jubilee
Date: Sunday Oct 2, 2022
When: 2-4 p.m.
Location: Brindle9 Alehouse
413 Marlowe Ct #200, Sacramento, CA 95821
Tickets: www.Tixolvo.com
General seating: $15 for adults and $10 for students

```html
<!DOCTYPE html>
<html lang="en">
<head>
<meta charset="utf-8">
<title>HarmoNest Ensemble Jubilee</title>
<link rel="stylesheet" href="https://fonts.googleapis.com/css2?family=Oswald:wght@600&family=Open+Sans:wght@600;700&family=Playball&family=Lora:ital,wght@1,400;1,500&display=swap">
<style>
  :root {
    --stage: #5f5f5f;
    --night-top: #1c1430;
    --violet: #3b2a52;
    --amber: #b07a3c;
    --rose: #b0506a;
    --navy: #1f1a5c;
    --navy-deep: #0d0b3e;
    --yellow: #fbf163;
    --white: #ffffff;
    --shadow: #1a1420;
  }
  * { margin: 0; padding: 0; box-sizing: border-box; }
  html, body { width: 1200px; height: 800px; overflow: hidden; }
  body { background: var(--stage); position: relative; }

  .banner {
    position: absolute; left: 0; top: 100px;
    width: 1200px; height: 600px; overflow: hidden;
  }
  .banner__photo {
    position: absolute; inset: 0;
    background:
      radial-gradient(ellipse 45% 30% at 30% 45%, rgba(200,150,80,.55), transparent 70%),
      radial-gradient(ellipse 40% 30% at 72% 48%, rgba(210,110,90,.5), transparent 70%),
      radial-gradient(ellipse 50% 25% at 50% 60%, rgba(190,80,120,.55), transparent 70%),
      linear-gradient(180deg, var(--night-top) 0%, var(--violet) 22%, var(--amber) 42%, var(--rose) 58%, var(--navy) 78%, var(--navy-deep) 100%);
  }

  .event-date {
    position: absolute; top: 30px; left: 958px;
    display: flex; align-items: center; gap: 10px;
    color: var(--white); font-family: "Lora", serif; font-style: italic;
  }
  .event-date__day { text-align: right; line-height: 1.05; }
  .event-date__day span { display: block; }
  .event-date__weekday { font-size: 16px; }
  .event-date__time { font-size: 20px; }
  .event-date__rule { width: 1px; height: 38px; background: var(--white); }
  .event-date__year { font-family: "Lora", serif; font-style: normal; font-size: 40px; font-weight: 500; }

  .title-script {
    position: absolute; top: 92px; left: 0; width: 100%;
    text-align: center; color: var(--white);
    font-family: "Playball", cursive; font-size: 84px; line-height: 1;
    text-shadow: 3px 3px 0 var(--shadow);
  }
  .title-block {
    position: absolute; top: 196px; left: 0; width: 100%;
    text-align: center; color: var(--yellow);
    font-family: "Oswald", sans-serif; font-weight: 600;
    font-size: 148px; line-height: 1; letter-spacing: 2px;
    text-shadow: 3px 3px 0 var(--shadow);
  }

  .venue {
    position: absolute; top: 352px; left: 0; width: 100%;
    text-align: center; color: var(--white);
    font-family: "Open Sans", sans-serif; font-weight: 600;
    font-size: 19px; line-height: 28px;
  }

  .tickets {
    position: absolute; top: 428px; left: 230px; width: 697px; height: 70px;
    border-top: 1.5px solid var(--white); border-bottom: 1.5px solid var(--white);
    display: flex; align-items: center;
    font-family: "Open Sans", sans-serif; font-weight: 700;
  }
  .tickets__seating {
    width: 185px; height: 100%;
    border-right: 1.5px solid var(--white);
    display: flex; flex-direction: column; justify-content: center;
    padding-left: 20px;
    color: var(--yellow); font-size: 27px; line-height: 28px;
  }
  .tickets__prices { display: flex; align-items: center; gap: 34px; padding-left: 16px; }
  .price { display: flex; align-items: center; gap: 14px; }
  .price__label { color: var(--white); font-size: 26px; letter-spacing: .5px; }
  .price__amount { color: var(--yellow); font-size: 40px; }

  .booking {
    position: absolute; top: 528px; left: 0; width: 100%;
    display: flex; justify-content: center; align-items: baseline; gap: 8px;
  }
  .booking__label { color: var(--yellow); font-family: "Lora", serif; font-style: italic; font-size: 31px; }
  .booking__url { color: var(--white); font-family: "Open Sans", sans-serif; font-weight: 600; font-size: 19px; letter-spacing: .45em; }
</style>
</head>
<body>
  <section class="banner">
    <div class="banner__photo" role="img" aria-label="Photo of a cheering concert crowd in silhouette against warm bokeh stage lights"></div>

    <div class="event-date">
      <div class="event-date__day">
        <span class="event-date__weekday">Sunday Oct 2</span>
        <span class="event-date__time">At 2-4 p.m.</span>
      </div>
      <div class="event-date__rule"></div>
      <div class="event-date__year">2022</div>
    </div>

    <h1>
      <span class="title-script">HarmoNest Ensemble</span>
      <span class="title-block">JUBILEE</span>
    </h1>

    <p class="venue">Brindle9 Alehouse<br>413 Marlowe Ct #200, Sacramento, CA 95821</p>

    <div class="tickets">
      <div class="tickets__seating"><span>GENERAL</span><span>SEATING</span></div>
      <div class="tickets__prices">
        <div class="price"><span class="price__label">ADULTS</span><span class="price__amount">$15</span></div>
        <div class="price"><span class="price__label">STUDENTS</span><span class="price__amount">$10</span></div>
      </div>
    </div>

    <p class="booking"><span class="booking__label">Booking on :-</span><span class="booking__url">www.Tixolvo.com</span></p>
  </section>
</body>
</html>
```